Flyer Design Project for The Amberfield Company

I'm a Naturopathic Herbalist who wishes to expand my business from x1 a week to x5 days a week and so need to produce a flyer to let people know what I do and to guide them to my website at theamberfieldcompany.com.au.
One-sided or double-sided A5 flyer on good quality paper for distribution by my referral network.  If all the info can fit on one side that would be great.
It would be great if the design could link up with my website i.e. the sun, mountains etc in the background but don't worry if not possible so then as an alternative I'd like to see something modern, fresh.
Otherwise it's to be simple, clean, easy to read, with a couple of relevant pictures if you want.

Target Market(s)
Predominantly females, from teens "clear skin tonics" to overloaded twenty-somethings, to pre-baby fertility programmes, healthy pregnancy etc
Industry/Entity Type
Business
Look and feel

```html
<!DOCTYPE html>
<html lang="en">
<head>
<meta charset="utf-8">
<title>Sick and Tired – Herbal Medicine Flyer</title>
<link href="https://fonts.googleapis.com/css2?family=Archivo+Black&family=Arimo:wght@400;700&family=Roboto:wght@100;300;700;900&display=swap" rel="stylesheet">
<style>
  :root {
    --leaf-green: #05ac55;
    --deep-green: #0b7a3c;
    --shadow-green: #064d26;
    --paper: #ffffff;
    --copy: rgba(255,255,255,0.92);
    --ink: #222222;
    --divider: rgba(255,255,255,0.55);
  }
  * { margin: 0; padding: 0; box-sizing: border-box; }
  html, body { width: 1200px; height: 852px; overflow: hidden; background: var(--leaf-green); }
  .flyer { position: relative; width: 1200px; height: 852px; background: var(--leaf-green); font-family: "Arimo", Arial, sans-serif; }
  .panel-divider { position: absolute; left: 599px; top: 0; width: 1px; height: 852px; background: var(--divider); }

  /* Cover panel */
  .cover { position: absolute; left: 0; top: 0; width: 599px; height: 852px; overflow: hidden; }
  .question-mark { position: absolute; left: 355px; top: -10px; font-family: "Roboto", Arial, sans-serif; font-weight: 900; font-size: 330px; line-height: 1; color: var(--paper); }
  .headline-sick { position: absolute; left: 150px; top: 128px; font-family: "Roboto", Arial, sans-serif; font-weight: 300; font-size: 150px; line-height: 1; color: var(--paper); letter-spacing: -2px; }
  .headline-and { position: absolute; left: 220px; top: 258px; font-family: "Roboto", Arial, sans-serif; font-weight: 300; font-size: 54px; line-height: 1; color: var(--paper); }
  .headline-tired { position: absolute; left: 82px; top: 268px; font-family: "Archivo Black", Arial, sans-serif; font-size: 142px; line-height: 1; color: var(--paper); letter-spacing: -3px; }
  .subhead { position: absolute; left: 116px; top: 392px; font-family: "Arimo", Arial, sans-serif; font-size: 22.5px; line-height: 22px; color: var(--paper); text-transform: uppercase; letter-spacing: 0.2px; }
  .herb-scene { position: absolute; left: 0; top: 455px; width: 599px; height: 397px; background: linear-gradient(180deg, var(--leaf-green) 0%, var(--deep-green) 35%, var(--shadow-green) 62%, var(--deep-green) 82%, var(--leaf-green) 100%); }

  /* Inside panel */
  .copy-column { position: absolute; top: 56px; width: 232px; font-size: 12.6px; line-height: 23.5px; color: var(--copy); text-align: justify; }
  .copy-column p { margin-bottom: 23.5px; }
  .copy-column--first { left: 652px; }
  .copy-column--second { left: 917px; }
  .copy-column .compact { line-height: 16px; margin-bottom: 22px; }
  .copy-column .web { font-weight: 700; color: var(--paper); }

  .contact-card { position: absolute; left: 0; top: 0; width: 1200px; height: 852px; pointer-events: none; }
  .contact-text { position: absolute; left: 717px; top: 685px; width: 365px; text-align: center; color: var(--ink); font-size: 13.2px; line-height: 18px; }
  .contact-name { font-family: "Arimo", Arial, sans-serif; font-weight: 700; font-size: 16.5px; color: var(--leaf-green); line-height: 20px; }
</style>
</head>
<body>
<main class="flyer">
  <section class="cover">
    <div class="question-mark">?</div>
    <div class="headline-sick">Sick</div>
    <div class="headline-and">and</div>
    <div class="headline-tired">Tired</div>
    <p class="subhead">Herbal medicine could<br>be the answer for you.</p>
    <div class="herb-scene" role="img" aria-label="Fresh herb sprigs and a blue dropper bottle rising from rippling water"></div>
  </section>

  <div class="panel-divider"></div>

  <section class="copy-column copy-column--first">
    <p>Maren has a wealth of experience with over 14 years in clinical practice which, coupled with a great deal of “life experience” as the mother of three children, helps to make your consultation professional, caring and healing.</p>
    <p>Passionate about helping you reach your highest potential health-wise, Maren will make you a “Daily Wellness Tonic” which is like the best multi-vitamin you could have as it’s tailor-made especially for you. The “Daily Wellness Tonic” can help strengthen, nourish, heal and rebalance your whole body.</p>
    <p>“Daily Wellness Tonics” can be made to assist you keeping yourself well, for nurturing yourself (so in turn you can nurture others), for re-energising you, for aging gracefully, to assist you feeling back on top of life and to help you face challenges more easily.</p>
  </section>

  <section class="copy-column copy-column--second">
    <p>Herbal medicine can help with Sleep Disorders, Weak Immune Systems, Anxiety, Depression, Fertility issues, Childhood Diseases, Skin Problems, Gastro-Intestinal Disorders and Women’s Health.</p>
    <p class="compact" style="line-height:22.5px">Maren also specialises in “Super Immune Boost Tonics” assisting with acute conditions such as coughs, colds, sore throats and offers 20-30 minute “Express Appointments”. Useful as a preventative measure or as a way of healing these conditions more quickly.</p>
    <p class="compact">“Clear Skin Wellness Tonics” are popular with teens and a special teen package is also offered as an “Express Appointment” with a bottle of tonic.</p>
    <p class="compact">For more information, check out The Amberfield Company website at <span class="web">www.theamberfieldcompany.com.au</span></p>
  </section>

  <svg class="contact-card" viewBox="0 0 1200 852" aria-hidden="true">
    <polygon fill="#ffffff" points="717,656 897,656 897,676 1082,676 1082,767 959,767 959,793 738,793 738,767 717,767"/>
  </svg>
  <address class="contact-text" style="font-style:normal">
    <div class="contact-name">Maren Holt DHM,</div>
    Local Naturopathic Herbalist<br>
    joins the professional team at Fernleaf Wellbeing Rooms<br>
    48 Harbour Lane, Westmere, NSW, 2099<br>
    Ph: 0400 316 582
  </address>
</main>
</body>
</html>
```